Flyer Design Project for Brightwater Wellbeing Rooms

We are a psychology clinic that specialises in eating, parenting and chronic illness & pain. See our website for a summary.

We need a flyer that will go to doctors and schools in the local area.

Things to include on the front page:

Immediate appointments available
After hours appointments available
Male and female psychologists

Phone 9563 2190
Web brightwaterwellbeingrooms.com.au

On the back page:

Phone 9563 2190
Suite 1/1287 Marlowe Rd, Kelverton East 3185.
brightwaterwellbeingrooms.com.au

Parenting: Parenthood is an amazing journey, but for lots of people it raises all sorts of issues from fear of birth, breastfeeding difficulties and settling problems, to toddler discipline and food fussiness all the way through to getting help for your depressed or anxious adolescent. Our Parenting Psychologists can help you be the best parent you can be which will in turn lead to happier families, homes, children and parents.

Chronic illness/pain: Diabetes, heart disease, arthritis, asthma, migraines, dizziness, chronic fatigue syndrome, infertility, and PCOS are just some of the conditions that can be managed with psychological interventions. Everything we do is about helping you to manage your condition and get back to focusing on what you really want your life to be about.

Eating: Whether you suffer from anorexia, bulimia or binge eating, our strategies help you develop a healthy relationship with food and your body. The practical tips and strategies that we can provide are very useful for people undergoing lapband surgery or liposuction.

I am interested in whether the photographs that I have already purchased can be used...so please have a look through the website and see which you think will suit your design. Photographs are not absolutely necessary though, so if it doesn't fit with your idea that is okay too.
Updates

HI Everyone,

Thanks for submitting so far! I haven't found anything yet that has hit the mark. And I am thinking that is my fault and maybe that way i have described what I want. I apologise and hope that this update might help.

This brochure is likely to sit with lots of other brochures in a doctors waiting room so it needs to be different - so that it will be noticed.

The majority of our market are women - so something feminine is important. Maybe it needs to be a little more playful that I had initially thought. Like maybe not your standard blocky text and bolds and primary colours. But something more creative, more personal.

I want to not focus just on the family theme. Parenting is one area that we cover, but also we help people with eating disorders and chronic illness/chronic pain. So the photographs that I use need to be more general. It is importnat to focus on happy and healthy looking people. As we went to appeal to what my potential clients want to look like and feel like.

I do hope this helps to guide you. I promise that once I see a flyer that I could choose, I will turn the funding to guaranteed. I did this last time...I am just a bit nervous as I haven't received anything yet that I am excited about.

Kindest regards,

Marnie.

Hi Everyone,

Thank you for your designs coming in! As promised, as soon as I received a design that I could see myself choosing I would change the status from refundable to committed. I have now done this!

I have received a design that I would say is good. It is not perfect however...so please keep the ideas coming.

To give more direction, the one that came in has a nice theme that runs through the brochure. Not too many different types of font and colours detracting from the flow of the flyer. However, the thing that I am concerned about is whether it will stand out enough on a rack of other flyers in a doctors waiting room.

I hope this helps with your creative ideas.

Thanks again to everyone!

Marnie.

Thanks SO much to everyone who is putting in designs. You are making my decision difficult!

I am wondering if you can update your designs with a few things:

can I ask you to make some text changes:

1. Can we have a heading on the front page: Psychologists  and then can you put Kelverton East in smaller writing just below it?

2. Id like to say on the front: Specialising in parenting, disordered eating and chronic pain & illness

3. Delete Male & Female Psychologists

4. In general we dont' need to have the logo standing out. We don't have a well known brand yet, so I am not wanting to take up valuable space with this - so perhaps it shoudl be small and maybe just on the back? Keeping the name of our clinic on the front with the website shoudl be sufficient.

Thanks heaps everyone...I will make decision very soon!

Target Market(s)

20-40 year olds. Working. Educated. Female. They might have a family/children.
Australian. Engish speaking.

Industry/Entity Type

Clinic

Requirements
Must have
• I would like to include our logo. Please do not use the colour green that it is in. I hate that colour! but I LOVE the logo.

I would like to follow through with some of the themes of the website and other stationary.

I will attach some of the other stationary I have had designed.

I really like the colours in the letterhead - especially that blue of the logo.

I think it needs to have a dash of colour with it at least...something that will stand out and be noticed on a brochure rack...but also have a look of class/sophistication/modern.
Nice to have
• Perhaps photograph of happy and healthy people.
Should not have
• I don't like bold text or too many different types of fonts.

It shouldn't look too cluttered so I might need to reduce the text I have included - I will need to see it first.

```html
<!DOCTYPE html>
<html lang="en">
<head>
<meta charset="utf-8">
<title>Brightwater Wellbeing Rooms – Flyer</title>
<link rel="stylesheet" href="https://fonts.googleapis.com/css2?family=Source+Sans+3:wght@400;600&display=swap">
<style>
  :root {
    --stage: #000000;
    --panel-grey: #f2f2f4;
    --panel-white: #ffffff;
    --orange: #e8902a;
    --band-orange: #e38d25;
    --ink: #2c2c2c;
    --muted: #5a5a5a;
    --green: #1d7a5c;
    --slate: #3a3a3c;
  }
  * { box-sizing: border-box; margin: 0; padding: 0; }
  html, body {
    width: 1200px; height: 1176px; overflow: hidden;
    background: var(--stage);
    font-family: "Source Sans 3", "Myriad Pro", Arial, sans-serif;
  }
  .canvas { position: relative; width: 1200px; height: 1176px; }

  .panel {
    position: absolute; top: 81px; width: 466px; height: 987px;
    overflow: hidden;
  }
  .panel--back { left: 111px; background: var(--panel-grey); }
  .panel--front {
    left: 636px;
    background: linear-gradient(180deg, #e9e9ea 390px, #ffffff 700px, #ffffff 100%);
  }

  /* Back panel */
  .services { position: absolute; left: 40px; top: 46px; width: 393px; }
  .service {
    font-size: 14.6px; line-height: 23px; color: var(--ink);
    text-align: justify; margin-bottom: 33px;
  }
  .service__title {
    color: var(--orange); font-size: 26px; line-height: 23px;
    font-weight: 400; margin-right: 4px;
  }
  .back-photo { position: absolute; left: 0; top: 642px; width: 466px; height: 228px; }
  .back-contact {
    position: absolute; left: 0; right: 0; top: 888px;
    text-align: center; color: var(--muted); font-size: 14.6px; line-height: 21px;
  }
  .back-contact__web { color: var(--orange); font-size: 19px; margin-top: 8px; display: block; }

  /* Front panel */
  .front-photo { position: absolute; left: 0; top: 0; width: 466px; height: 320px; }
  .offers {
    position: absolute; left: 0; right: 0; top: 343px;
    text-align: center; color: var(--orange);
    font-size: 34px; line-height: 39px; letter-spacing: -0.2px;
  }
  .offers__item { margin-bottom: 23px; }
  .clinic-name {
    position: absolute; left: 74px; top: 740px;
    display: flex; align-items: center; gap: 18px;
  }
  .clinic-name__dot {
    width: 64px; height: 64px; border-radius: 50%;
    border: 5px solid var(--green);
  }
  .clinic-name__text {
    color: #7a7a7c; font-size: 21px; line-height: 27px;
    letter-spacing: 4px; text-transform: uppercase;
  }
  .front-swoosh { position: absolute; left: 0; bottom: 0; width: 466px; height: 150px; }
  .front-contact {
    position: absolute; left: 0; right: 0; top: 908px;
    text-align: center; color: #111; font-size: 19.5px; line-height: 30px;
  }
  .front-contact__phone { font-weight: 600; font-size: 23px; }
</style>
</head>
<body>
<div class="canvas">

  <section class="panel panel--back">
    <div class="services">
      <p class="service"><span class="service__title">Parenting:</span> Parenthood is an amazing journey, but for lots of people it raises all sorts of issues from fear of birth, breastfeeding difficulties and settling problems, to toddler discipline and food fussiness all the way through to getting help for your depressed or anxious adolescent. Our Parenting Psychologists can help you be the best parent you can be which will in turn lead to happier families, homes, children and parents.</p>
      <p class="service"><span class="service__title">Chronic illness / pain:</span> Diabetes, heart disease, arthritis, asthma, migraines, dizziness, chronic fatigue syndrome, infertility, and PCOS are just some of the conditions that can be managed with psychological interventions. Everything we do is about helping you to manage your condition and get back to focusing on what you really want your life to be about.</p>
      <p class="service"><span class="service__title">Eating:</span> Whether you suffer from anorexia, bulimia or binge eating, our strategies help you develop a healthy relationship with food and your body. The practical tips and strategies that we can provide are very useful for people undergoing lapband surgery or liposuction.</p>
    </div>

    <svg class="back-photo" role="img" aria-label="Photo of a smiling family of four huddled together under a blue sky" viewBox="0 0 466 228" preserveAspectRatio="none">
      <defs>
        <linearGradient id="familySky" x1="0" y1="0" x2="0" y2="1">
          <stop offset="0" stop-color="#5f9fd6"/>
          <stop offset="0.55" stop-color="#b9d6ee"/>
          <stop offset="1" stop-color="#d9c3b3"/>
        </linearGradient>
      </defs>
      <rect width="466" height="228" fill="url(#familySky)"/>
    </svg>

    <div class="back-contact">
      Phone&nbsp; - 9563 2190<br>
      Suite 1/1287 Marlowe Rd, Kelverton East 3185.
      <span class="back-contact__web">www.brightwaterwellbeingrooms.com.au</span>
    </div>
  </section>

  <section class="panel panel--front">
    <svg class="front-photo" role="img" aria-label="Photo of a mother and toddler enjoying a picnic on green grass" viewBox="0 0 466 320" preserveAspectRatio="none">
      <defs>
        <linearGradient id="picnicGrass" x1="0" y1="0" x2="0" y2="1">
          <stop offset="0" stop-color="#9bc46a"/>
          <stop offset="0.5" stop-color="#6fa23f"/>
          <stop offset="1" stop-color="#a07a58"/>
        </linearGradient>
      </defs>
      <polygon points="0,0 466,0 466,265 0,311" fill="url(#picnicGrass)"/>
      <polygon points="0,311 466,265 466,276 0,322" fill="var(--slate)"/>
    </svg>

    <div class="offers">
      <p class="offers__item">Immediate<br>appointments available</p>
      <p class="offers__item">After hours<br>appointments available</p>
      <p class="offers__item">Male and female<br>psychologists</p>
    </div>

    <div class="clinic-name">
      <span class="clinic-name__dot"></span>
      <span class="clinic-name__text">Brightwater<br>Wellbeing<br>Rooms</span>
    </div>

    <svg class="front-swoosh" viewBox="0 0 466 150" preserveAspectRatio="none" aria-hidden="true">
      <path d="M0,55 C140,40 300,25 466,0 L466,30 C300,48 150,58 0,62 Z" fill="var(--green)"/>
      <path d="M0,66 C150,62 300,52 466,34 L466,150 L0,150 Z" fill="var(--band-orange)"/>
    </svg>

    <div class="front-contact">
      Contact us - <span class="front-contact__phone">9563 2190</span><br>
      www.brightwaterwellbeingrooms.com.au
    </div>
  </section>

</div>
</body>
</html>
```